Fast Money - Simple Book Cover Design

Hello,

I am in need of a cover for my new book. The Book Title Is

"Standing Growth - Keys to Glowing Customer Ratings That Fill The Calendar and Draw Fresh Clients Through Every Entrance!"

Author: Fireman Dale Orsworth

What I want: This is a book for businesses on improving their online reputation. I want to have 5 Stars on the cover. You can look at this quarvex search for ideas of what I am meaning.....

(copy and paste)

http://www.quarvex-find.example/search?q=5+star+online+reviews&mode=images&ref=kx7Lp2QwZt9 (copy and paste)

I am open to different color schemes for the book. I am partial to dark blues if you make it look good. Here is another book that I really like the cover of....

http://www.brindlemart.example/Clipwave-Tactics-Earning-Promotion-ebook/item/Z93KT4WQPX

I want the cover BOLD and to STAND OUT.

I am looking for a design to help establish me as an authority for online reputation marketing. This book will be both in Pagely format and be used in print as well.

I am open to questions....

Thanks!

Dale

Reason: I don't believe we have received the right designs. I am going to give everyone more time...

Reason: Hi everyone, I had some stuff come up and was not able to be involved in this project. I am extending because we have not seen the exact thing we want and need time to work with designers to get it right. Thanks Dale

Reason: I am currently traveling and can't wrap this up until I get back.

Target Market(s)

Business Owners

Industry/Entity Type

Business

Requirements
Must have
• Title and Subtitle

Author Name

5 Stars Images....
Nice to have
• Creativity

Bold and stand out

Professional

Should not have
• thin text, small to read text, lame graphics,

```html
<!DOCTYPE html>
<html lang="en">
<head>
<meta charset="utf-8">
<title>Standing Growth – Book Cover</title>
<link rel="stylesheet" href="https://fonts.googleapis.com/css2?family=Roboto+Condensed:wght@700&family=Roboto:wght@700&display=swap">
<style>
  :root {
    --page: #ffffff;
    --sky-top: #e4e4e8;
    --sky-mid: #8f98a8;
    --slate: #3a5165;
    --star: #f2ea45;
    --ghost: rgba(255, 255, 255, 0.10);
    --band-deep: #16667f;
    --band-teal: #007b9b;
    --band-light: #a9e0f7;
    --ink-light: #ffffff;
  }
  html, body {
    margin: 0;
    padding: 0;
    width: 1200px;
    height: 900px;
    overflow: hidden;
    background: var(--page);
  }
  .cover {
    position: absolute;
    left: 308px;
    top: 0;
    width: 585px;
    height: 900px;
    overflow: hidden;
    background: linear-gradient(to bottom, var(--sky-top) 0%, var(--sky-mid) 28%, var(--slate) 55%, var(--slate) 100%);
  }
  .numeral-area {
    position: absolute;
    left: 120px;
    top: 67px;
    width: 410px;
    height: 510px;
    border-radius: 40% 40% 50% 50%;
    background: radial-gradient(ellipse at center, var(--ghost) 0%, rgba(255,255,255,0.05) 55%, rgba(255,255,255,0) 75%);
  }
  .growth-area {
    position: absolute;
    left: 0;
    top: 560px;
    width: 585px;
    height: 340px;
    background: linear-gradient(to bottom,
      rgba(58,81,101,0) 0%,
      var(--band-deep) 22%,
      var(--band-teal) 45%,
      var(--band-light) 68%,
      var(--page) 86%,
      var(--page) 100%);
  }
  .stars {
    position: absolute;
    left: 0;
    top: 0;
  }
  .title {
    position: absolute;
    left: 42px;
    top: 178px;
    margin: 0;
    font-family: "Roboto Condensed", "Arial Narrow", sans-serif;
    font-weight: 700;
    font-size: 128px;
    line-height: 102px;
    letter-spacing: 0.5px;
    color: var(--ink-light);
  }
  .subtitle {
    position: absolute;
    left: 47px;
    top: 410px;
    width: 430px;
    margin: 0;
    font-family: "Roboto", Arial, sans-serif;
    font-weight: 700;
    font-size: 20px;
    line-height: 34px;
    color: var(--ink-light);
  }
  .author {
    position: absolute;
    left: 0;
    width: 100%;
    top: 869px;
    margin: 0;
    text-align: center;
    font-family: "Roboto", Arial, sans-serif;
    font-weight: 700;
    font-size: 17px;
    color: var(--slate);
  }
</style>
</head>
<body>
  <main class="cover">
    <div class="numeral-area" role="img" aria-label="Faint oversized numeral five behind the title"></div>
    <div class="growth-area" role="img" aria-label="Layered rising zigzag growth graphic in teal and light blue"></div>

    <svg class="stars" width="585" height="200" viewBox="0 0 585 200" aria-label="Five stars">
      <defs>
        <polygon id="star" points="0,-40 9.4,-12.9 38,-12.4 15.2,4.9 23.5,32.4 0,16 -23.5,32.4 -15.2,4.9 -38,-12.4 -9.4,-12.9"
                 fill="var(--star)" stroke="#ffffff" stroke-width="1.5"/>
      </defs>
      <use href="#star" x="157" y="106"/>
      <use href="#star" x="229" y="129"/>
      <use href="#star" x="301" y="106"/>
      <use href="#star" x="373" y="129"/>
      <use href="#star" x="445" y="106"/>
    </svg>

    <h1 class="title">Standing<br>Growth</h1>
    <p class="subtitle">Keys to glowing customer ratings that fill the calendar and draw fresh clients through every entrance!</p>

    <p class="author">Fireman Dale Orsworth</p>
  </main>
</body>
</html>
```